Sticker olive oil

Good day,
I would like to design a sticker that will be stuck on an olive oil bottle. It should have the manufacturer's picture on it (in the background, as a hologram, ....?). The brand is a made-up word, composed of the name of the producer "Marceno" and the Italian "Olio" for oil. So composed: Verdalune; the double "O" in the middle could be represented as an olive, then there is an immediate reference to the olive oil. Other textual content should be:
Main brand: "Verdalune"
Description: "cold pressed, pure olive oil from the Valle - Prino (Castelmira)
Addition: "guaranteed untreated"
You can reach me via my email info@rovetka.de
Payment via PayPal; budget 50 €
I'm still trying to upload the current label, the picture of Marceno too

Logo Text

Verdalune

```html
<!DOCTYPE html>
<html lang="en">
<head>
<meta charset="utf-8">
<title>Verdalune – Olive Oil Label</title>
<link rel="stylesheet" href="https://fonts.googleapis.com/css2?family=Besley:wght@700&family=Montserrat:wght@500;600&display=swap">
<style>
  :root {
    --backdrop: #0e0d0b;
    --label-paper: #f4f3ef;
    --ink-dark: #1c1b18;
    --ink-olive: #5e5a3a;
    --gold: #c9a43e;
    --portrait-light: #f1efe3;
    --portrait-tone: #dcdcbf;
  }
  html, body {
    margin: 0;
    padding: 0;
    width: 920px;
    height: 1200px;
    overflow: hidden;
    background: var(--backdrop);
  }
  .canvas {
    position: relative;
    width: 920px;
    height: 1200px;
  }
  .label {
    position: absolute;
    left: 190px;
    top: 60px;
    width: 540px;
    height: 1080px;
    font-family: "Montserrat", sans-serif;
  }
  .label-shape {
    position: absolute;
    inset: 0;
  }
  .producer-portrait {
    position: absolute;
    left: 125px;
    top: 145px;
    width: 290px;
    height: 335px;
    border-radius: 46% 46% 12% 12%;
    background: radial-gradient(ellipse at 50% 38%, var(--portrait-tone) 0%, var(--portrait-light) 62%, var(--label-paper) 100%);
  }
  .brand-name {
    position: absolute;
    left: 0;
    width: 540px;
    top: 492px;
    margin: 0;
    text-align: center;
    font-family: "Besley", serif;
    font-weight: 700;
    font-size: 76px;
    line-height: 1;
    letter-spacing: -1px;
    color: var(--ink-dark);
  }
  .descriptor {
    position: absolute;
    left: 0;
    width: 540px;
    margin: 0;
    text-align: center;
    text-transform: uppercase;
    line-height: 1;
  }
  .descriptor--process {
    top: 610px;
    font-size: 21px;
    font-weight: 500;
    letter-spacing: 1.5px;
    color: var(--ink-olive);
  }
  .descriptor--product {
    top: 653px;
    font-size: 22px;
    font-weight: 500;
    letter-spacing: 3.5px;
    color: var(--gold);
    display: flex;
    justify-content: center;
    align-items: center;
    gap: 20px;
  }
  .descriptor--product .rule {
    width: 30px;
    height: 1px;
    background: var(--gold);
  }
  .descriptor--origin {
    top: 706px;
    font-size: 15px;
    font-weight: 600;
    letter-spacing: 2.5px;
    line-height: 1.35;
    color: var(--ink-olive);
  }
  .quality-seal {
    position: absolute;
    left: 185px;
    top: 775px;
    width: 170px;
    height: 170px;
  }
</style>
</head>
<body>
<main class="canvas">
  <section class="label">
    <svg class="label-shape" viewBox="0 0 540 1080" width="540" height="1080" aria-hidden="true">
      <path d="M270,0 C470,150 540,330 540,540 C540,750 470,930 270,1080 C70,930 0,750 0,540 C0,330 70,150 270,0Z" fill="var(--label-paper)"/>
      <path d="M270,22 C455,165 518,340 518,540 C518,740 455,915 270,1058 C85,915 22,740 22,540 C22,340 85,165 270,22Z" fill="none" stroke="var(--gold)" stroke-width="1.5"/>
    </svg>

    <div class="producer-portrait" role="img" aria-label="Faint engraved-style portrait of the producer Marceno"></div>

    <h1 class="brand-name">Verdalune</h1>

    <p class="descriptor descriptor--process">Cold Pressed</p>
    <p class="descriptor descriptor--product"><span class="rule"></span>Pure Olive Oil<span class="rule"></span></p>
    <p class="descriptor descriptor--origin">From the Valle Ortesa<br>-Castelmira-</p>

    <svg class="quality-seal" viewBox="0 0 170 170" width="170" height="170">
      <defs>
        <path id="seal-arc-top" d="M30,85 A55,55 0 0 1 140,85"/>
        <path id="seal-arc-bottom" d="M20,85 A65,65 0 0 0 150,85"/>
      </defs>
      <text font-family="Montserrat, sans-serif" font-size="14" font-weight="500" letter-spacing="2.5" fill="var(--ink-olive)">
        <textPath href="#seal-arc-top" startOffset="50%" text-anchor="middle">GUARANTEED</textPath>
      </text>
      <text font-family="Montserrat, sans-serif" font-size="14" font-weight="500" letter-spacing="2.5" fill="var(--ink-olive)">
        <textPath href="#seal-arc-bottom" startOffset="50%" text-anchor="middle">UNTREATED</textPath>
      </text>
      <line x1="22" y1="78" x2="22" y2="92" stroke="var(--ink-olive)" stroke-width="1"/>
      <line x1="148" y1="78" x2="148" y2="92" stroke="var(--ink-olive)" stroke-width="1"/>
      <circle cx="85" cy="85" r="21" fill="var(--gold)"/>
    </svg>
  </section>
</main>
</body>
</html>
```